BrivoLane Ute.

I want the full logo on one side. And the other side the card if right Ralf the logo the left half orange like the car in the logo color with Danielle R Morrow
Founder and CEO
Email symbol then dmorrow@brivolaneute.com
Www symbol. Then Brivolaneute.com
Phone symbol then 413-926-BRIV
The very bottom would like Brivo Lane Ute is a division of Harmond Vistas. LLC

```html
<!DOCTYPE html>
<html lang="en">
<head>
<meta charset="utf-8">
<title>Brivo Lane Ute – Business Card</title>
<link rel="stylesheet" href="https://fonts.googleapis.com/css2?family=Lato:wght@400;700&family=Crimson+Text:ital@1&display=swap">
<style>
  :root {
    --backdrop: #222222;
    --card-white: #ffffff;
    --brand-orange: #e88d2a;
    --ink: #1f1f1f;
    --ink-soft: #2a2a2a;
    --card-shadow: rgba(0, 0, 0, 0.55);
  }
  * { margin: 0; padding: 0; box-sizing: border-box; }
  html, body {
    width: 1200px;
    height: 900px;
    overflow: hidden;
    background: var(--backdrop);
  }
  .canvas {
    position: relative;
    width: 1200px;
    height: 900px;
    background: var(--backdrop);
  }
  .card {
    position: absolute;
    top: 200px;
    width: 310px;
    height: 502px;
    box-shadow: 4px 4px 4px var(--card-shadow);
  }
  .card-front {
    left: 253px;
    background: var(--card-white);
    border-radius: 62px 0 62px 0;
    font-family: "Lato", sans-serif;
    color: var(--ink);
  }
  .card-back {
    left: 627px;
    width: 309px;
    background: var(--brand-orange);
    border-radius: 0 70px 0 70px;
  }
  .brand-mark {
    position: absolute;
    top: 180px;
    left: 0;
    width: 100%;
    display: flex;
    align-items: center;
    justify-content: center;
    gap: 9px;
  }
  .brand-dot {
    width: 16px;
    height: 16px;
    border-radius: 50%;
    background: var(--brand-orange);
  }
  .brand-name {
    font-family: "Lato", sans-serif;
    font-weight: 700;
    font-size: 25px;
    letter-spacing: 0.5px;
    color: var(--ink);
  }
  .holder {
    position: absolute;
    left: 32px;
    top: 339px;
  }
  .holder-name {
    font-weight: 700;
    font-size: 17px;
    color: var(--brand-orange);
    text-transform: uppercase;
    line-height: 20px;
  }
  .holder-title {
    font-size: 14px;
    line-height: 17px;
    color: var(--ink-soft);
  }
  .contact-list {
    position: absolute;
    left: 32px;
    top: 410px;
    list-style: none;
  }
  .contact-item {
    display: flex;
    align-items: center;
    gap: 5px;
    font-size: 14px;
    line-height: 18px;
    color: var(--ink-soft);
  }
  .contact-icon {
    width: 12px;
    height: 12px;
    flex: none;
  }
  .division-note {
    position: absolute;
    top: 150px;
    left: 0;
    width: 100%;
    text-align: center;
    font-family: "Crimson Text", serif;
    font-style: italic;
    font-size: 37px;
    line-height: 51px;
    color: var(--ink);
  }
</style>
</head>
<body>
<main class="canvas">
  <section class="card card-front" aria-label="Card front">
    <div class="brand-mark">
      <span class="brand-dot" aria-hidden="true"></span>
      <span class="brand-name">BRIVO LANE UTE</span>
    </div>

    <div class="holder">
      <p class="holder-name">Danielle R Morrow</p>
      <p class="holder-title">Founder and CEO</p>
    </div>

    <ul class="contact-list">
      <li class="contact-item">
        <svg class="contact-icon" viewBox="0 0 12 12" aria-hidden="true">
          <path d="M1 4.5 Q6 0.5 11 4.5 L9.5 6 L8 4.8 L4 4.8 L2.5 6 Z" fill="var(--brand-orange)"/>
          <rect x="2.5" y="6.5" width="7" height="4.5" rx="1" fill="var(--brand-orange)"/>
        </svg>
        <span>413-926-BRIV</span>
      </li>
      <li class="contact-item">
        <svg class="contact-icon" viewBox="0 0 12 12" aria-hidden="true">
          <rect x="0.5" y="2" width="11" height="8" rx="1" fill="var(--brand-orange)"/>
          <path d="M1 2.8 L6 6.8 L11 2.8" fill="none" stroke="#fff" stroke-width="1"/>
        </svg>
        <span>dmorrow@brivolaneute.com</span>
      </li>
      <li class="contact-item">
        <svg class="contact-icon" viewBox="0 0 12 12" aria-hidden="true">
          <circle cx="6" cy="6" r="5.5" fill="var(--brand-orange)"/>
          <path d="M3.5 3.5 Q5 4.5 4.5 6.5 Q6.5 7 6 9.5 M7.5 2 Q7 4 9 4.5" fill="none" stroke="#fff" stroke-width="1"/>
        </svg>
        <span>www.brivolaneute.com</span>
      </li>
    </ul>
  </section>

  <section class="card card-back" aria-label="Card back">
    <p class="division-note">Brivo Lane Ute<br>is a division of<br>Harmond<br>Vistas. LLC</p>
  </section>
</main>
</body>
</html>
```